Flyer for 1 day Lean Manufacturing event

I have: 2 sample flyers for the same event, a Word document with the text I would like to use, photos to include. Not all photos need to be included.

I would like a 2 (maybe 1?) page flyer I can use for marketing this and future events. Can be MS Publisher format, or other as preferred - please provide PDF also just in case.

```html
<!DOCTYPE html>
<html lang="en">
<head>
<meta charset="utf-8">
<title>One Day Lean Manufacturing Simulation Flyer</title>
<link rel="stylesheet" href="https://fonts.googleapis.com/css2?family=Montserrat:wght@300;400;500;600;700;800;900&family=Barlow+Condensed:wght@500;600;700&display=swap">
<style>
:root{
  --bg:#272629;
  --blue:#2a57ac;
  --blue-dark:#1d3f86;
  --green:#12a84a;
  --green-light:#25b955;
  --red:#bd2127;
  --orange:#d85a24;
  --white:#ffffff;
  --ink:#2b2b2b;
  --body:#3a3a3a;
  --font-main:'Montserrat',sans-serif;
  --font-cond:'Barlow Condensed',sans-serif;
}
*{box-sizing:border-box;margin:0;padding:0}
html,body{width:1200px;height:800px;overflow:hidden;background:var(--bg);font-family:var(--font-main);color:var(--ink)}
.canvas{position:relative;width:1200px;height:800px}
.side-label{position:absolute;top:34px;color:var(--white);font-family:var(--font-main);font-weight:700;font-size:18px;letter-spacing:7px}
.side-label.front{left:283px}
.side-label.back{left:849px}
.page{position:absolute;background:var(--white);overflow:hidden}
.page-front{left:72px;top:66px;width:516px;height:667px}
.page-back{left:625px;top:67px;width:513px;height:664px}
.stripes{position:absolute;left:0;width:100%;height:4px;display:flex;gap:4px}
.stripes i{flex:1;display:block}
.stripes i:nth-child(1){background:var(--red)}
.stripes i:nth-child(2){background:var(--green)}
.stripes i:nth-child(3){background:var(--orange)}

/* Front */
.hero{position:absolute;left:0;top:0;width:100%;height:235px;background:linear-gradient(120deg,var(--blue-dark) 0%,var(--blue) 55%,#3a66b8 100%)}
.hero-title{position:absolute;left:102px;top:48px;color:var(--white);font-weight:800;line-height:.9}
.hero-title .l1{display:block;font-size:63px;letter-spacing:-1px}
.hero-title .l2{display:block;font-size:24px;margin-top:7px;letter-spacing:-.3px}
.hero-title .l3{display:block;font-size:46px;margin-top:5px;letter-spacing:-.5px}
.powered{position:absolute;left:106px;top:179px;width:374px;display:flex;align-items:center;gap:8px;color:var(--white);font-size:15.5px;font-weight:400;white-space:nowrap}
.powered::before,.powered::after{content:"";flex:1;height:1px;background:var(--white)}
.feature{position:absolute;left:41px;top:266px;width:444px;height:174px;display:flex}
.feature-photo{width:202px;height:100%;background:linear-gradient(135deg,#8a8f95,#4d5a6a 60%,#2e4f9a)}
.feature-panel{flex:1;background:linear-gradient(120deg,var(--green) 0%,var(--green-light) 100%);color:var(--white);padding:22px 18px 0 25px}
.feature-panel .kicker{font-size:19px;font-weight:300;line-height:1.1}
.feature-panel .bang{font-size:26px;font-weight:600;line-height:1.15;margin-bottom:10px}
.feature-panel p{font-size:11px;font-weight:300;line-height:1.2}
.intro-cols{position:absolute;left:41px;top:468px;width:412px;display:flex;gap:24px}
.intro-cols p{font-size:10.8px;font-weight:400;line-height:1.16;color:var(--body)}
.intro-cols p:first-child{width:204px}
.intro-cols p:last-child{width:184px}
.footer-band{position:absolute;left:0;bottom:0;width:100%;height:68px;background:linear-gradient(100deg,var(--red) 60%,#c82a2e 100%)}
.brand-box{position:absolute;background:var(--white);display:flex;align-items:center;justify-content:center;text-align:center;color:var(--red);font-family:var(--font-cond);font-weight:700;line-height:1}
.front .brand-box{left:38px;top:571px;width:76px;height:76px;font-size:17px}
.register-now{position:absolute;left:131px;top:612px;color:var(--white);font-family:var(--font-cond);font-weight:700;font-size:33px;letter-spacing:.3px}
.social{position:absolute;color:var(--white);font-family:var(--font-cond);font-weight:600;font-size:15px;letter-spacing:.5px}
.front .social{left:368px;top:624px}

/* Back */
.back-head{position:absolute;left:0;top:0;width:100%;height:57px;background:linear-gradient(120deg,var(--blue-dark),var(--blue))}
.back-head h2{position:absolute;left:51px;top:18px;color:var(--white);font-size:16px;font-weight:700;letter-spacing:-.2px;white-space:nowrap}
.covered{position:absolute;left:30px;top:78px;width:332px;font-size:9.9px;line-height:1.2;font-weight:400;letter-spacing:-.15px;color:var(--body)}
.covered p{margin-bottom:4px}
.takeaways{position:absolute;left:30px;top:163px;width:248px;list-style:none}
.takeaways li{position:relative;padding-left:15px;font-size:8.5px;line-height:1.28;font-weight:400;letter-spacing:-.2px;margin-bottom:9.5px;color:var(--body)}
.takeaways li::before{content:"";position:absolute;left:2px;top:3px;width:4px;height:4px;border-right:1.6px solid var(--orange);border-top:1.6px solid var(--orange);transform:rotate(45deg)}
.takeaways b{font-weight:700;color:var(--ink)}
.takeaways .justify{text-align:justify}
.bio{position:absolute;left:293px;top:153px;width:198px;height:266px;background:var(--green);color:var(--white);text-align:center;padding:36px 10px 0}
.headshot{position:absolute;left:345px;top:90px;width:96px;height:96px;border-radius:50%;border:5px solid var(--green);background:linear-gradient(160deg,#c9ccd0,#7d848c)}
.bio h3{font-size:15.5px;font-weight:700;margin-bottom:7px}
.bio p{font-size:7.9px;font-weight:400;line-height:1.27;margin-bottom:8px}
.register{position:absolute;left:293px;top:427px;width:198px;height:237px;background:var(--white);border:1px solid #eee}
.register-head{position:relative;height:40px;background:var(--orange);color:var(--white);font-family:var(--font-cond);font-weight:700;font-size:24px;text-align:center;line-height:40px;letter-spacing:.4px}
.register-head::after{content:"";position:absolute;left:28px;bottom:-6px;border-left:6px solid transparent;border-right:6px solid transparent;border-top:6px solid var(--orange)}
.details{list-style:none;padding:13px 0 0 25px}
.details li{display:flex;gap:9px;margin-bottom:9px;font-family:var(--font-cond);font-size:11.2px;line-height:1.05;color:#333;font-weight:600}
.details svg{flex:none;width:16px;height:16px}
.details .label{display:block;color:var(--orange);font-weight:700}
.page-back .footer-band{width:293px;height:68px}
.back .brand-box{left:30px;top:577px;width:76px;height:70px;font-size:17px}
.back .social{left:135px;top:620px}
</style>
</head>
<body>
<div class="canvas">
  <div class="side-label front">FRONT</div>
  <div class="side-label back">BACK</div>

  <section class="page page-front front">
    <div class="hero" role="img" aria-label="Blue-tinted photo of participants at a workshop table"></div>
    <h1 class="hero-title"><span class="l1">ONE DAY</span><span class="l2">LEAN MANUFACTURING</span><span class="l3">SIMULATION</span></h1>
    <div class="powered">Powered by Lean Ladder</div>
    <div class="stripes" style="top:237px"><i></i><i></i><i></i></div>

    <div class="feature">
      <div class="feature-photo" role="img" aria-label="Photo of participants assembling blue and green block products at a workshop table"></div>
      <div class="feature-panel">
        <div class="kicker">Start the year</div>
        <div class="bang">with a bang!</div>
        <p>Our one day Lean and TOC Simulation shows you how to integrate Lean into your process, and demonstrates how you can lead or support successful implementation.</p>
      </div>
    </div>

    <div class="intro-cols">
      <p>The Simulation recreates the manufacturing environment through the hands-on assembly of "products" at separate work stations and all participants work together to refine the process and achieve optimum output. (Challenge: try to beat the standing record)</p>
      <p>By applying best practice techniques under practical conditions, participants will accelerate awareness and understanding that will enhance the success rate and effectiveness of your Lean program.</p>
    </div>

    <div class="footer-band"></div>
    <div class="brand-box">Lean<br>Ladder</div>
    <div class="register-now">REGISTER NOW!</div>
    <div class="social">@leanladder</div>
  </section>

  <section class="page page-back back">
    <div class="back-head"><h2>What will be covered and what you will take away</h2></div>
    <div class="stripes" style="top:60px"><i></i><i></i><i></i></div>

    <div class="covered">
      <p>How to rate your company using a Manufacturing Excellence model, and use the model to drive improvement.</p>
      <p>How to maximise productivity using the Theory of Constraints.</p>
      <p>The application of lean methodologies across manufacturing, financials, administration and the supply chain.</p>
    </div>

    <ul class="takeaways">
      <li>Ability to list, discuss and review process issues by using basic <b>problem solving techniques</b></li>
      <li>How to identify and <b>eliminate non-value added</b> activities.</li>
      <li>How to distinguish between push and <b>pull systems</b> and understand the control method of <b>Kanban</b> pull signals to balance supply and demand, improve lead times and reduce work-in progress.</li>
      <li>Understand why, when, and how to practice <b>set up time reduction.</b></li>
      <li>Why large <b>batch sizes</b> are not cost effective and increase inventory, lead times, and reduce flexibility.</li>
      <li>Why consistent processes give quality results through <b>standard work</b> practices and procedures.</li>
      <li>The importance of <b>visual performance measures</b> in driving behaviours.</li>
      <li>How the implementation of <b>5S housekeeping</b> is the cornerstone of best practice.</li>
      <li>The importance of quality at source and <b>mistake proofing.</b></li>
      <li>Why <b>preventative and autonomous maintenance</b> is critical to overall equipment effectiveness.</li>
      <li class="justify">Understand the key best practices areas of: <b>Leading and Managing Change, Teamwork, Set-up Reduction, Process and Material Flow, Focused Improvement, 5S, and Visual Performance Measures.</b></li>
    </ul>

    <div class="bio">
      <h3>Daniel Hartley</h3>
      <p>is a skilled consultant, specialising in maximising profit, capacity and unlocking production efficiency.</p>
      <p>He is a professional engineer with 18 years of consulting experience in production system design, continuous improvement tools and rapid interventions.</p>
      <p>Prior to entering consulting he gained wide-ranging experience in the Australian automotive industry implementing Lean and other World Class practices across the supply chain including Parts and Accessory, Tier 1 Supply, and Vehicle Assembly Plant. He is also a specialist in Inventory Optimisation, Energy Optimisation, Excel Auditing, and the Supply Chain Operations Reference (SCOR) Model</p>
    </div>
    <div class="headshot" role="img" aria-label="Portrait photo of the presenter"></div>

    <div class="footer-band"></div>
    <div class="brand-box">Lean<br>Ladder</div>
    <div class="social">@leanladder</div>

    <div class="register">
      <div class="register-head">REGISTER HERE</div>
      <ul class="details">
        <li>
          <svg viewBox="0 0 16 16" fill="none" stroke="#d85a24" stroke-width="1.1"><rect x="1.5" y="3" width="13" height="11.5" rx="1"/><path d="M1.5 6.5h13M5 1.5v3M11 1.5v3"/><path d="M4 9h1.5M7.3 9h1.5M10.5 9H12M4 11.8h1.5M7.3 11.8h1.5"/></svg>
          <span><span class="label">Date:</span>Friday 16th February 2024</span>
        </li>
        <li>
          <svg viewBox="0 0 16 16" fill="none" stroke="#d85a24" stroke-width="1.1"><circle cx="8" cy="8" r="6.5"/><path d="M8 4v4l2.8 1.8"/></svg>
          <span><span class="label">Time:</span>8am to 5pm</span>
        </li>
        <li>
          <svg viewBox="0 0 16 16" fill="none" stroke="#d85a24" stroke-width="1.1"><path d="M2 11h12M3 11a5 5 0 0 1 10 0M8 5V3.5M1.5 13.5h13"/></svg>
          <span><span class="label">Catering provided</span></span>
        </li>
        <li>
          <svg viewBox="0 0 16 16" fill="none" stroke="#d85a24" stroke-width="1.1"><path d="M8 15s5-5 5-8.5a5 5 0 0 0-10 0C3 10 8 15 8 15z"/><circle cx="8" cy="6.5" r="1.8"/></svg>
          <span><span class="label">Venue:</span>Lakeview Hotel, Harbour Room<br>12 Meadowbank Drive<br>Brookfield QLD 4069</span>
        </li>
        <li>
          <svg viewBox="0 0 16 16" fill="none" stroke="#d85a24" stroke-width="1.1"><circle cx="9" cy="5.5" r="4"/><path d="M9 3.5v4M8 4.5h1.8a.8.8 0 0 1 0 1.6H8.2a.8.8 0 0 0 0 1.6H10"/><path d="M1 12.5l3-1.5h4l2 1 4-2"/></svg>
          <span><span class="label">Cost:</span>$350 per person incl GST</span>
        </li>
      </ul>
    </div>
  </section>
</div>
</body>
</html>
```